Web Design Pell Marrow

• An Overview of Pell Marrow for reference: We use to be a component manufacturing company. We sold to customers in USA and manage the builds in China using many manufacturing partners. We had a web site that served this market but we have transitioned over the last several years into “A unique design, development and program management company” It is this message we want to put up on the web now. We provide the design support, we help develop and test a new product for our customers and we provide the manufactured produce once we have transitioned it into production.
• The Target Market: Our customers are all high tech. Each product we produce is custom designed and sold only to one a specific customer. We work with a limited number of customer and sell to new customers by word of mouth and referrals. The web site is to provide a back ground check of any new referral so they can see who we are and our basic capabilities. It is not designed to sell customers or to find new customers but provide a background check to new potential customers.
• Pages Required: We estimate 12:
o Home/Title page is page 1 of PDF. It would have buttons to select other pages
o Names of other pages would be (short titles below if on button, if pull down menu the full title of slide)
 USA Facilities
 China Facilities
 Enclosures
 Antennas
 Connectors
 Cables
 EMI Shields
 Overlays
 Process Development
 Voxtrel
 Contact Us (???) >> new page which we are not sure if we should or should not add.
• Design Specifics; attached is our logo, a PDF and PowerPoint slides showing the views we desire. We like these layouts, but perhaps a better one may be suggested for some artistic reason or layout. It should be clean, simple and user intuitive. We like the off white background and use for most of our presentations. One should be able to go from any screen to any other screen. The quote must include both design and implementation onto our web site which is http://pellmarrowsystems.com/
• Design Process:
We would like to see concepts of the Landing/Homepage, and an internal page initially. Feedback will be provided and you will be asked to continue if your layout is on the correct track.

• Implementation: Desire designer/implimentor to set up on their server. Allow us to test and edit on their site. We will provide password for implementation on our site after final approval.

Target Market(s)

• The Target Market: see above task descripiton

Industry/Entity Type

It Company

Requirements
Must have
• • Pages Required: We estimate 12:
 USA Facilities
 China Facilities
 Enclosures
 Antennas
 Connectors
 Cables
 EMI Shields
 Overlays
 Process Development
 Voxtrel

Must have the implementation phase include in quote. see task description above
Should not have
• Should not be complex or long time loading.
Do not want any twitter or promotional add on functions.

```html
<!DOCTYPE html>
<html lang="en">
<head>
<meta charset="utf-8">
<title>Pell Marrow Technologies</title>
<link rel="stylesheet" href="https://fonts.googleapis.com/css2?family=Montserrat:wght@400;600;700;800&family=Oswald:wght@700&display=swap">
<style>
:root{
  --blue:#0a72bd;
  --navy:#333a6b;
  --grey:#6b6b6b;
  --map:#efefef;
  --line:#e3e3e3;
  --bg:#ffffff;
}
*{box-sizing:border-box;margin:0;padding:0}
html,body{width:1200px;height:885px;overflow:hidden;background:var(--bg)}
body{position:relative;font-family:"Montserrat",sans-serif;color:var(--grey)}
.abs{position:absolute}
.call{left:161px;top:47px;display:flex;align-items:center;gap:10px}
.call-label{font-size:11.5px;color:var(--grey)}
.call-number{font-size:17px;font-weight:600;color:var(--blue)}
.nav{top:84px;height:56px;background:var(--navy);display:flex;align-items:center;justify-content:space-around}
.nav::after{content:"";position:absolute;left:8%;right:8%;bottom:-10px;height:12px;border-radius:50%;background:rgba(0,0,0,.28);filter:blur(6px);z-index:-1}
.nav a{color:#fff;text-decoration:none;font-size:11px;font-weight:700;letter-spacing:-.2px}
.nav .sep{width:1px;height:16px;border-left:1px dotted rgba(255,255,255,.45)}
.nav-left{left:160px;width:336px}
.nav-right{left:668px;width:372px}
.top-links{right:168px;top:59px;font-size:9.5px;font-weight:600;color:var(--blue);letter-spacing:.3px}
.top-links span{margin:0 7px}
.brand{left:515px;top:37px;width:136px;height:137px;display:flex;flex-direction:column;align-items:center;justify-content:center;gap:8px;text-align:center}
.brand-square{width:34px;height:34px;background:var(--blue)}
.brand-name{font-size:19px;font-weight:800;color:var(--blue);line-height:1.05;text-transform:uppercase}
.world{left:200px;top:176px;width:800px;height:384px;border-radius:40px;background:radial-gradient(ellipse at center,#ececec 0%,#f4f4f4 60%,#fbfbfb 100%)}
.pin{width:42px;height:52px}
.address{font-size:9px;font-weight:600;color:var(--blue);line-height:11.5px}
.headline{left:250px;top:506px;font-family:"Oswald",sans-serif;font-weight:700;line-height:44px;letter-spacing:-.5px;text-transform:uppercase}
.headline .l1{display:block;font-size:44px;color:var(--blue)}
.headline .l2{display:block;font-size:48px;color:var(--navy)}
.rule{left:160px;width:880px;height:0;border-top:1px dotted #d9d9d9}
.col{top:654px}
.col h2{font-size:18.5px;font-weight:700;color:var(--blue);letter-spacing:-.8px;margin-bottom:14px}
.col p,.col li{font-size:10.4px;line-height:13.6px;color:var(--grey)}
.col ul{list-style:none}
.col li{line-height:19px}
.btn{display:inline-block;background:var(--blue);color:#fff;font-size:10px;font-weight:700;border-radius:4px;height:21px;line-height:21px;text-align:center;text-decoration:none;letter-spacing:-.3px}
.vdiv{top:656px;height:132px;border-left:1px dotted #dcdcdc}
.field{width:237px;height:29px;border:1px solid #d4d4d4;border-radius:7px;display:flex;align-items:center;font-size:11.5px;color:var(--grey)}
.field .ico{width:42px;display:flex;justify-content:center;border-right:1px dotted #bbb;height:15px;align-items:center;margin-right:11px}
.footer-links{left:180px;top:828px;font-size:10.4px;color:var(--grey)}
.copyright{left:180px;top:852px;font-size:9.5px;font-weight:600;color:#8a8a8a}
.copyright a{color:var(--blue);text-decoration:none;margin-left:4px}
</style>
</head>
<body>

<div class="abs call">
  <svg width="27" height="27" viewBox="0 0 27 27" aria-hidden="true"><circle cx="13.5" cy="13.5" r="12.5" fill="none" stroke="#333a6b" stroke-width="1.5"/><path d="M16 7c-1 0-2 1-2.5 2l1.5 1.5c-.8 1.8-1.8 3.5-3 5L10.5 15c-1 .6-1.5 1.8-1 2.8l1 1.5c3.5-1.5 6.5-6.5 6.5-11z" fill="#333a6b"/></svg>
  <span class="call-label">Call Us TODAY:</span>
  <span class="call-number">0800 2002 3000</span>
</div>

<nav class="abs nav nav-left">
  <a href="#">USA FACILITIES</a><span class="sep"></span>
  <a href="#">CHINA FACILITIES</a><span class="sep"></span>
  <a href="#">ENCLOSURES</a>
</nav>

<div class="abs top-links">OVERLAYS<span>|</span>PROCESS DEVELOPMENT<span>|</span>VOXTREL<span>|</span>CONTACT US</div>

<nav class="abs nav nav-right">
  <a href="#">ANTENNAS</a><span class="sep"></span>
  <a href="#">CONNECTORS</a><span class="sep"></span>
  <a href="#">CABLES</a><span class="sep"></span>
  <a href="#">EMI SHIELDS</a>
</nav>

<div class="abs brand">
  <span class="brand-square"></span>
  <span class="brand-name">Pell Marrow<br>Technologies</span>
</div>

<div class="abs world" role="img" aria-label="Light grey world map showing the company's locations in the USA and China"></div>

<div class="abs address" style="left:325px;top:298px">48 Alder Crest Road<br>Suite 210 Marlow Bay, CA<br>95990</div>
<svg class="abs pin" style="left:284px;top:324px" viewBox="0 0 42 52" aria-hidden="true"><ellipse cx="21" cy="49" rx="9" ry="2.5" fill="rgba(0,0,0,.15)"/><path d="M21 2C10 2 2 10 2 20c0 10 19 28 19 28s19-18 19-28C40 10 32 2 21 2z" fill="#d8331f"/><circle cx="21" cy="18" r="7" fill="#7d1308"/></svg>

<div class="abs address" style="left:810px;top:257px">Qinghe Tech Park<br>Building 7 Xinhe Road Beijing, China<br>100085</div>
<svg class="abs pin" style="left:848px;top:283px" viewBox="0 0 42 52" aria-hidden="true"><ellipse cx="21" cy="49" rx="9" ry="2.5" fill="rgba(0,0,0,.15)"/><path d="M21 2C10 2 2 10 2 20c0 10 19 28 19 28s19-18 19-28C40 10 32 2 21 2z" fill="#d8331f"/><circle cx="21" cy="18" r="7" fill="#7d1308"/></svg>

<h1 class="abs headline"><span class="l1">A unique design, development and</span><span class="l2">program management company</span></h1>

<div class="abs rule" style="top:625px"></div>

<section class="abs col" style="left:181px;width:260px">
  <h2>WHO WE ARE?</h2>
  <p>Lorem ipsum dolor sit amet, consectetuer adipiscing elit, sed diam nonummy nibh euismod tincidunt ut laoreet dolore magna aliquam erat volutpat.</p>
  <a class="btn" href="#" style="width:80px;margin-top:11px;margin-left:-1px">Read More...</a>
</section>

<div class="abs vdiv" style="left:453px"></div>

<section class="abs col" style="left:480px;width:250px">
  <h2>OUR PRODUCTS</h2>
  <ul>
    <li>Custom Enclosure Design and Development</li>
    <li>Custom Antenna Design and Development</li>
    <li>Custom Connector Design and Development</li>
  </ul>
  <a class="btn" href="#" style="width:102px;margin-top:6px">More Products...</a>
</section>

<div class="abs vdiv" style="left:748px"></div>

<section class="abs col" style="left:780px;width:240px">
  <h2 style="margin-left:2px">SIGN UP WITH US</h2>
  <div class="field"><span class="ico"><svg width="17" height="13" viewBox="0 0 17 13" aria-hidden="true"><rect x="1" y="3" width="15" height="9" fill="#444"/><path d="M1 3l7.5 5L16 3" fill="none" stroke="#fff" stroke-width="1.3"/><path d="M4 3V1h9v2" fill="none" stroke="#444" stroke-width="1.2"/></svg></span>Enter Your Email Address</div>
  <div class="field" style="margin-top:4px"><span class="ico"><svg width="15" height="15" viewBox="0 0 15 15" aria-hidden="true"><circle cx="10" cy="5" r="3.6" fill="#444"/><path d="M8 7L2 13M3.5 11.5l1.5 1.5M5 10l1.3 1.3" stroke="#444" stroke-width="1.8" fill="none"/></svg></span>Enter Your Password</div>
  <a class="btn" href="#" style="width:80px;margin-top:7px;margin-left:1px">Login</a>
</section>

<div class="abs rule" style="top:810px"></div>

<div class="abs footer-links">USA Facilities - China Facilities - Enclosures - Antennas - Connectors - Cables - EMI Shields - Overlays - Process Development - Voxtrel - &nbsp;Contact Us</div>
<div class="abs copyright">PELL MARROW TECHNOLOGIES © 2013 - <a href="#">Privacy Policy</a></div>

</body>
</html>
```